Super Greens Label for Supplement Bottle

We want to design a front label for a health supplement bottle. The product is called Meadow Twist Chews™. This will be a new product so there is no current website for the product. The focus is on supergreens that taste great and deliver support for energy, digestion, and immune defense.
We want it to be modern, vibrant and appealing.
Bottle size: standard size supplement CLEAR bottle size, with white child resistant cap and the label panel dimensions are 3” x 7”. The label should be primarily white and green, with a touch of red; (see color palettes)/it can also ONLY be white and green. See samples attached.
We are only focused on the front of the bottle design, not on the back, but leave space for the supplement panel and other text on the back.
So the text for the front of the bottle is:
RT Balden's
Meadow Twist Chews™
Super Greens Blend for:
Energy, Digestion, and Immune Support*
60 Gummies | Dietary Supplement
Raspberry Flavor Gummies
Off to side of the label:
Non-GMO
Vegan Friendly
Plant-Based
Gelatin Free
Colors
Designer to choose colors to be used in the design.

```html
<!DOCTYPE html>
<html lang="en">
<head>
<meta charset="utf-8">
<title>Meadow Twist Chews – Front Label</title>
<link rel="stylesheet" href="https://fonts.googleapis.com/css2?family=Fredoka:wght@600&family=Barlow+Semi+Condensed:wght@500&display=swap">
<style>
  :root {
    --page-bg: #f4f4f4;
    --green-deep: #1f7a4e;
    --green-mid: #3fa876;
    --green-light: #8fd3b2;
    --green-mist: #a8dfc4;
    --white: #ffffff;
    --raspberry: #c7445a;
    --gummy-green: #5cb98c;
  }
  * { margin: 0; padding: 0; box-sizing: border-box; }
  html, body {
    width: 1200px;
    height: 899px;
    overflow: hidden;
    background: var(--page-bg);
  }
  .canvas {
    position: relative;
    width: 1200px;
    height: 899px;
  }
  .label {
    position: absolute;
    left: 291px;
    top: 84px;
    width: 618px;
    height: 730px;
    overflow: hidden;
  }
  .label-art {
    position: absolute;
    inset: 0;
    background:
      radial-gradient(ellipse at 55% 55%, var(--green-mist) 0%, var(--green-light) 22%, transparent 48%),
      radial-gradient(ellipse at 75% 20%, var(--green-deep) 0%, transparent 40%),
      radial-gradient(ellipse at 20% 85%, var(--green-deep) 0%, transparent 45%),
      linear-gradient(160deg, var(--green-mid), var(--green-deep));
  }
  .label-graphics {
    position: absolute;
    inset: 0;
  }
  .product-name {
    position: absolute;
    left: 100px;
    width: 400px;
    top: 250px;
    text-align: center;
    font-family: "Fredoka", sans-serif;
    font-weight: 600;
    font-size: 54px;
    line-height: 58px;
    color: var(--white);
  }
  .product-name sup {
    font-size: 22px;
    vertical-align: top;
    line-height: 1;
  }
  .benefits {
    position: absolute;
    left: 0;
    right: 0;
    top: 411px;
    text-align: center;
    font-family: "Barlow Semi Condensed", sans-serif;
    font-weight: 500;
    font-size: 15.5px;
    line-height: 21px;
    color: var(--white);
  }
  .count {
    position: absolute;
    left: 114px;
    top: 520px;
    display: flex;
    align-items: baseline;
    gap: 5px;
    color: var(--white);
  }
  .count-number {
    font-family: "Fredoka", sans-serif;
    font-weight: 600;
    font-size: 50px;
    line-height: 50px;
  }
  .count-detail {
    font-family: "Barlow Semi Condensed", sans-serif;
    font-weight: 500;
    font-size: 11.5px;
  }
  .flavor-text {
    font-family: "Barlow Semi Condensed", sans-serif;
    font-weight: 500;
    font-size: 8.5px;
    fill: var(--white);
  }
</style>
</head>
<body>
  <main class="canvas">
    <section class="label">
      <div class="label-art" role="img" aria-label="Abstract glossy green gummy shapes filling the label background"></div>

      <svg class="label-graphics" width="618" height="730" viewBox="0 0 618 730">
        <g fill="none" stroke="var(--white)" stroke-width="2.5">
          <path d="M203 154 H100 V576 H193"/>
          <path d="M500 242 V576 H363"/>
          <path d="M245 386 H356" stroke-width="1.2"/>
        </g>
        <circle cx="455" cy="580" r="27" fill="var(--gummy-green)" role="img" aria-label="Green gummy"/>
        <circle cx="451" cy="540" r="23" fill="var(--raspberry)" role="img" aria-label="Raspberry"/>
        <defs>
          <path id="flavor-arc" d="M419 545 A34 34 0 1 1 487 545"/>
        </defs>
        <text class="flavor-text"><textPath href="#flavor-arc" startOffset="2">Raspberry Flavor Gummies</textPath></text>
      </svg>

      <h1 class="product-name">Meadow Twist<br>Chews<sup>™</sup></h1>

      <p class="benefits">Super Greens Blend for:<br>Energy, Digestion, and Immune Support*</p>

      <div class="count">
        <span class="count-number">60</span>
        <span class="count-detail">Gummies | Dietary Supplement</span>
      </div>
    </section>
  </main>
</body>
</html>
```